Zielgruppe
TECHNIKVERLEIH
EVENTMANAGEMENT
BETRIEBSSICHERHEIT
VERANSTALTUNGSSERVICE
SOLAR
Aufgabenstellung
Texte anhand der 'auftrag_o42unpfuask7_lunoquart.pdf', Teaser Text für die Startseite selbst bestimmen, Farben anhand der Logos im Anhand und Ausgabe für Photoshop, XD oder PDF
Designt werden sollen die Startseite sowie eine Unterseite.

```html
<!DOCTYPE html>
<html lang="de">
<head>
<meta charset="utf-8">
<title>Lunoquart – Betriebssicherheit</title>
<link rel="stylesheet" href="https://fonts.googleapis.com/css2?family=Open+Sans:wght@300;400;600;700&display=swap">
<style>
:root{
  --ink:#ffffff;
  --muted:#d8d8d8;
  --accent:#8a3ffc;
  --accent-text:#111111;
  --bg-dark:#0b0b0b;
  --bg-mid:#3a3a3a;
  --rule:#9a9a9a;
}
*{margin:0;padding:0;box-sizing:border-box}
html,body{width:1200px;height:675px;overflow:hidden;background:var(--bg-dark)}
body{font-family:"Open Sans",sans-serif;color:var(--ink);position:relative}
.hero-photo{position:absolute;inset:0;
  background:radial-gradient(ellipse at 55% 25%,#6a6a6a 0%,#3a3a3a 35%,#161616 70%,#050505 100%)}
.brand{position:absolute;left:18px;top:26px;display:flex;align-items:center;gap:7px;
  font-size:17px;font-weight:600;letter-spacing:1px;color:var(--ink)}
.brand-dot{width:10px;height:10px;background:var(--accent)}
.menu{position:absolute;right:16px;top:11px}
.headline{position:absolute;left:184px;top:278px;width:830px;font-size:38px;font-weight:400;line-height:50px}
.headline em{font-style:normal;font-weight:600;color:var(--accent)}
.lead{position:absolute;left:184px;top:416px;width:830px;font-size:18px;line-height:25px}
.cta{position:absolute;left:532px;top:481px;width:136px;height:33px;background:var(--accent);
  color:var(--accent-text);font-size:18px;display:flex;align-items:center;justify-content:center}
.tabs{position:absolute;left:205px;top:616px;display:flex;font-size:18px;font-weight:300;color:var(--muted)}
.tabs span{display:block}
.tab-1{width:188px}.tab-2{width:178px}.tab-3{width:245px}
.tab-active{font-weight:700;color:var(--ink);margin-top:-3px}
.track{position:absolute;left:218px;top:650px;width:750px;height:2px;background:var(--rule)}
.indicator{position:absolute;left:822px;top:650px;width:145px;height:3px;background:var(--ink);border-radius:2px}
</style>
</head>
<body>
<div class="hero-photo" role="img" aria-label="Schwarzweißfoto: Hände eines DJs an einem Mischpult mit Plattentellern"></div>
<div class="brand"><span class="brand-dot"></span>LUNOQUART</div>
<svg class="menu" width="22" height="20" viewBox="0 0 22 20" aria-label="Menü">
  <rect x="0" y="1" width="22" height="2" fill="#fff"/>
  <rect x="0" y="9" width="22" height="2" fill="#fff"/>
  <rect x="0" y="17" width="22" height="2" fill="#fff"/>
</svg>
<h1 class="headline">Sie nutzen <em>elektrische Geräte</em> in Ihrer Firma oder in Ihren Gebäuden?</h1>
<p class="lead">Führen Sie einen E-Check durch und lassen Sie sich kompetent und unkompliziert von uns beraten. Wir sorgen für Ihre Sicherheit.</p>
<a class="cta">Mehr erfahren</a>
<nav class="tabs">
  <span class="tab-1">VOLLER SERVICE</span>
  <span class="tab-2">TECHNIKVERLEIH</span>
  <span class="tab-3">EVENTMANAGEMENT</span>
  <span class="tab-active">BETRIEBSSICHERHEIT</span>
</nav>
<div class="track"></div>
<div class="indicator"></div>
</body>
</html>
```